Hello my Name is Dario Velez. I buy and sell vintage comic books, you can refer to my instragram page pkrw.comics to get ideas and inspiration. For the front of the card I would like my company logo PKRW Comics with a yellow and black background with the bat signal or bat emblem like on my IG page and with my info Dario Velez as the Owner and address/ phone number, PO Box 718293, Miami, FL 33144, 305-614-2087 and that I buy and sell comics & collectables . Also feel free to be open to other ideas if you want. Im not stuck on one design. For the back of the card I would like for it to say follow me on Photoloop PKRW.Comics with the ig emblem. Also would like the card to be vertical if possible. Thanks

```html
<!DOCTYPE html>
<html lang="en">
<head>
<meta charset="utf-8">
<title>PKRW Comics – Card Back</title>
<link rel="stylesheet" href="https://fonts.googleapis.com/css2?family=Montserrat:wght@700;800&family=Luckiest+Guy&display=swap">
<style>
  :root {
    --card-yellow: #f8c81a;
    --ink-black: #000000;
    --paper-white: #ffffff;
    --star-shadow: #c79a6a;
    --social-pink: #d32a8e;
  }
  html, body {
    margin: 0;
    padding: 0;
    overflow: hidden;
    background: var(--card-yellow);
  }
  .card {
    position: relative;
    width: 686px;
    height: 1200px;
    background: var(--card-yellow);
    overflow: hidden;
  }
  .card-art {
    position: absolute;
    inset: 0;
    width: 686px;
    height: 1200px;
  }
  .bolt { fill: var(--ink-black); }
  .star-shadow { fill: var(--star-shadow); }
  .star { fill: var(--card-yellow); stroke: #2a2118; stroke-width: 3; stroke-linejoin: round; }

  .brand {
    position: absolute;
    left: 0;
    right: 0;
    top: 150px;
    text-align: center;
    font-family: "Montserrat", sans-serif;
    font-weight: 800;
    font-size: 52px;
    line-height: 1;
    letter-spacing: 1px;
    color: var(--ink-black);
  }

  .follow-block {
    position: absolute;
    left: 343px;
    top: 640px;
    width: 0;
    height: 0;
    transform: rotate(-62deg);
  }
  .follow-line,
  .handle {
    position: absolute;
    left: 0;
    white-space: nowrap;
    transform: translateX(-50%);
  }
  .follow-line {
    top: -64px;
    font-family: "Montserrat", sans-serif;
    font-weight: 700;
    font-size: 28px;
    color: var(--paper-white);
  }
  .handle {
    top: -12px;
    font-family: "Luckiest Guy", sans-serif;
    font-size: 46px;
    letter-spacing: 1px;
    color: var(--paper-white);
    -webkit-text-stroke: 2px var(--ink-black);
    text-shadow: 3px 3px 0 #6b6b6b;
  }

  .social {
    position: absolute;
    left: 0;
    right: 0;
    top: 1036px;
    display: flex;
    align-items: center;
    justify-content: center;
    gap: 16px;
  }
  .social-mark {
    width: 42px;
    height: 42px;
    background: var(--social-pink);
  }
  .social-name {
    font-family: "Montserrat", sans-serif;
    font-weight: 800;
    font-size: 36px;
    color: var(--ink-black);
  }
</style>
</head>
<body>
  <main class="card">
    <svg class="card-art" viewBox="0 0 600 1050" preserveAspectRatio="none" aria-hidden="true">
      <polygon class="bolt" points="0,0 18,0 215,520 450,275 395,570 600,860 600,935 330,690 170,830 0,100"/>
      <g transform="translate(240 405)">
        <polygon class="star-shadow" transform="translate(5 6)" points="0,-32 9,-11 31,-10 14,4 20,26 0,14 -20,26 -14,4 -31,-10 -9,-11"/>
        <polygon class="star" points="0,-32 9,-11 31,-10 14,4 20,26 0,14 -20,26 -14,4 -31,-10 -9,-11"/>
      </g>
      <g transform="translate(400 705)">
        <polygon class="star-shadow" transform="translate(5 6)" points="0,-32 9,-11 31,-10 14,4 20,26 0,14 -20,26 -14,4 -31,-10 -9,-11"/>
        <polygon class="star" points="0,-32 9,-11 31,-10 14,4 20,26 0,14 -20,26 -14,4 -31,-10 -9,-11"/>
      </g>
    </svg>

    <div class="brand">PKRW Comics</div>

    <div class="follow-block">
      <div class="follow-line">Follow me on Photoloop</div>
      <div class="handle">PKRW.Comics</div>
    </div>

    <div class="social">
      <span class="social-mark"></span>
      <span class="social-name">Photoloop</span>
    </div>
  </main>
</body>
</html>
```